nine-parts.com

We are a small dollar lending company that will revolutionize the industry. We will do this by being completely transparent, fee free, etc and an interest rate that normal people can afford to pay. Over 10X less than our competition. We only allow our members to pay bills " bills paid fast", within 72 hours. Payday loans typically charge from 390%-600% with a terrible payback structure. We charge 36%, period, with a payback structure over 12 months. Our site will be very simple and easy to use but elegant at the same time. We do not want the site to be too busy, less is more and easier. We will have; Home, The Story, Why 9parts.com, Are you eligible? Members, Clients. To become a member you have to be referred by a current client of 9parts.com. A lot of the busy stuff will be saved for the Members and Clients sections. The feel must be elegant, easy to use and very simple to understand. I am looking for the green, white and black combinations of colors, very similar to my logo that was designed by Pixelmoor.

```html
<!DOCTYPE html>
<html lang="en">
<head>
<meta charset="utf-8">
<title>nine-parts.com</title>
<link rel="stylesheet" href="https://fonts.googleapis.com/css2?family=Open+Sans:wght@400;600&family=Arimo:wght@400&display=swap">
<style>
  :root {
    --leaf: #8fc641;
    --ink: #1a1a1a;
    --paper: #ffffff;
    --hairline: #f1f1f1;
  }
  * { margin: 0; padding: 0; box-sizing: border-box; }
  html, body { width: 1200px; height: 809px; overflow: hidden; background: var(--paper); }
  .site {
    position: relative;
    width: 1200px;
    height: 809px;
    font-family: "Open Sans", Arial, sans-serif;
    color: var(--ink);
  }
  .edge-rule {
    position: absolute;
    left: 120px; top: 34px;
    width: 1px; height: 58px;
    background: var(--hairline);
  }
  .brand {
    position: absolute;
    left: 492px; top: 66px;
    display: flex;
    align-items: center;
    gap: 10px;
    font-family: "Open Sans", Arial, sans-serif;
    font-weight: 400;
    font-size: 22px;
    color: var(--ink);
    letter-spacing: -0.2px;
  }
  .brand-dot {
    width: 34px; height: 34px;
    border-radius: 50%;
    background: var(--leaf);
  }
  .main-nav {
    position: absolute;
    right: 658px;
    top: 182px;
    list-style: none;
    text-align: right;
  }
  .main-nav li {
    height: 67.6px;
    font-size: 17px;
    line-height: 24px;
    letter-spacing: 0.2px;
  }
  .main-nav a { color: var(--ink); text-decoration: none; }
  .main-nav .is-current a { color: var(--leaf); }
  .feature-panel {
    position: absolute;
    left: 568px; top: 181px;
    right: 0; bottom: 0;
    background: var(--leaf);
  }
  .promise-list {
    position: absolute;
    left: 328px;
    top: 214px;
    list-style: none;
    font-family: "Arimo", Arial, sans-serif;
    font-size: 13px;
    color: var(--paper);
  }
  .promise-list li { height: 33.8px; line-height: 16px; }
  .site-footer {
    position: absolute;
    top: 783px;
    left: 502px;
    font-family: "Arimo", Arial, sans-serif;
    font-size: 11.5px;
    display: flex;
  }
  .site-footer .label { width: 73px; color: var(--ink); }
  .site-footer .owner { color: var(--paper); }
  .site-footer .year { color: var(--paper); margin-left: 14px; }
</style>
</head>
<body>
<div class="site">
  <span class="edge-rule"></span>

  <header class="brand">
    <span class="brand-dot"></span>
    <span class="brand-name">nine-parts.com</span>
  </header>

  <nav>
    <ul class="main-nav">
      <li><a href="#">HOME</a></li>
      <li><a href="#">THE STORY</a></li>
      <li><a href="#">WHY NINE-PARTS.COM</a></li>
      <li class="is-current"><a href="#">ARE YOU ELIGIBLE ?</a></li>
      <li><a href="#">MEMBERS</a></li>
      <li><a href="#">CLIENTS</a></li>
    </ul>
  </nav>

  <main class="feature-panel">
    <ul class="promise-list">
      <li>36 %, NOT 390 - 600 %</li>
      <li>TRANSPARENT</li>
      <li>FEE FREE</li>
      <li>BILLS PAID WITHIN 72 HRS.</li>
      <li>PAYBACK STRUCTURE OVER 12 MONTHS</li>
    </ul>
  </main>

  <footer class="site-footer">
    <span class="label">Copyright :</span>
    <span class="owner">nine-parts.com</span>
    <span class="year">2014</span>
  </footer>
</div>
</body>
</html>
```